Brochure design for a Driftly Video Booth!

We are after a brochure for a Driftly Video Booth product being launched very soon. Attached are the logo, photos and all required information to be included in this brochure.

I have also attached a number of "inspiration" designs to show you the style we are after.

The colours should be black, white and a warm yellow (see attachment).

The brochure is for online use only, so does not need to constrain to typical printing specs. A square or rectangular booklet would be preferable.

Target Market(s)

Couples getting married between 20 - 35.

Industry/Entity Type

Printing

Font styles to use
Serif
Sans Serif

Colors
fece3e
000000
ffffff

Requirements
Must have
• at least 4 pages, a 'typography' design feel, good use of space. The colours should be black, white and a warm yellow (see attachment). Feel free to use whatever layout you think would work best.
Should not have
• Clutter.

```html
<!DOCTYPE html>
<html lang="en">
<head>
<meta charset="utf-8">
<title>Driftly Video Booth – Extras</title>
<link rel="stylesheet" href="https://fonts.googleapis.com/css2?family=Lobster&family=Tinos:wght@400;700&display=swap">
<style>
  :root {
    --black: #000000;
    --white: #ffffff;
    --yellow: #fece3e;
    --canvas: #e6e6e6;
    --photo-dark: #0b0b0b;
    --photo-mid: #3a3a3a;
  }
  * { margin: 0; padding: 0; box-sizing: border-box; }
  html, body {
    width: 1200px;
    height: 1000px;
    overflow: hidden;
    background: var(--canvas);
  }
  .page {
    position: absolute;
    left: 191px;
    top: 280px;
    width: 814px;
    height: 434px;
    background: var(--black);
    color: var(--white);
  }
  .rule {
    position: absolute;
    left: 35px;
    width: 745px;
    height: 4px;
    background: var(--white);
  }
  .rule--top { top: 34px; }
  .rule--bottom { top: 395px; }
  .photo {
    position: absolute;
    left: 0;
    top: 120px;
    width: 420px;
    height: 250px;
    background: radial-gradient(ellipse at 55% 60%, var(--photo-mid) 0%, var(--photo-dark) 70%);
  }
  .extras {
    position: absolute;
    left: 442px;
    top: 50px;
    width: 340px;
  }
  .extras__title {
    font-family: "Lobster", cursive;
    font-weight: 400;
    font-size: 22px;
    color: var(--yellow);
    margin-bottom: 28px;
  }
  .item__head {
    display: flex;
    align-items: baseline;
    margin-bottom: 8px;
  }
  .item__name {
    font-family: "Lobster", cursive;
    font-size: 20px;
    white-space: nowrap;
  }
  .item__leader {
    flex: 1;
    border-bottom: 1px dotted var(--white);
    margin: 0 5px;
    transform: translateY(-3px);
  }
  .item__price {
    font-family: "Tinos", serif;
    font-weight: 700;
    font-size: 17px;
    white-space: nowrap;
  }
  .item__text {
    font-family: "Tinos", serif;
    font-size: 12.5px;
    line-height: 17.3px;
    text-align: justify;
    padding-left: 15px;
    margin-bottom: 17px;
  }
  .item__text::before {
    content: "";
    display: inline-block;
    width: 5px;
    height: 5px;
    border-radius: 50%;
    background: var(--yellow);
    margin: 0 8px 2px 2px;
  }
</style>
</head>
<body>
  <section class="page">
    <div class="rule rule--top"></div>
    <div class="photo" role="img" aria-label="Black and white group photo of wedding guests laughing with props, with yellow liquid splashes"></div>
    <div class="extras">
      <h2 class="extras__title">Extras</h2>
      <article class="item">
        <div class="item__head">
          <span class="item__name">Additional Time</span>
          <span class="item__leader"></span>
          <span class="item__price">$300 per hour</span>
        </div>
        <p class="item__text">This includes the extra props and personal to get through each additional hour. For weddings 2 hours is the perfect time, however if you are booking the Driftly Booth for an event you may need more time depending on your events schedule.</p>
      </article>
      <article class="item">
        <div class="item__head">
          <span class="item__name">SFX Glass Bottles</span>
          <span class="item__leader"></span>
          <span class="item__price">$150</span>
        </div>
        <p class="item__text">This includes 4 special effects breakaway wine or beer bottles that you can smash across someone’s head, it doesn’t get any better then this! These bottles have been specially made to shatter on impact and they do not hurt. They are from an Australian special effects company.</p>
      </article>
    </div>
    <div class="rule rule--bottom"></div>
  </section>
</body>
</html>
```